Catalogue for Mobile charging stations with image and specifications about each model

I need a simple and clean catalogue that shows our products clearly with the specifications about them. something simple for potential clients to browse through and choose what fits their venue best.

I have attached 1 example of product page and 1 of the last page. This is just a reference on how simple and clean i want it, but you can design it however you want if you have a better idea. I want something professional

also i will attach our current logo (we will change it shortly but colors will remain the same so you can have an idea of color theme)
Updates

Project Deadline Extended Reason: Hello, i am extending this project by 5 days as I think only 5 days is too little Good luck everyone I'm looking forward to seeing all great designs!BestLiliana Added Tuesday, October 3, 2017

Target Market(s)

All types of companies

Font styles to use
Script

Colors

Designer to choose colors to be used in the design.

Requirements
Must have
• The catalogue will include about 60 products and specifications. I will provide you with images for all products and the specifications.
Nice to have
• A nice design that catches the viewers attention, not too complicated but simple and professional
• Our logo is green and black. so maybe best to stick with this color theme
• There are about 10 products missing from the files I sent with all the images and specification. These will be the last ones to be added as I am still waiting for some information
Should not have
• Too much design and patterns that makes it hard to focus on the product and information

```html
<!DOCTYPE html>
<html lang="en">
<head>
<meta charset="utf-8">
<title>VoltHarbor – VH-6 Charging Station</title>
<link rel="stylesheet" href="https://fonts.googleapis.com/css2?family=Arimo:wght@400;700&family=Michroma&family=Nunito:wght@600;700&display=swap">
<style>
  :root{
    --band-dark:#1c1c1c;
    --body-light:#a3a3a3;
    --body-mid:#7a7a7a;
    --body-deep:#555555;
    --teal:#3aa6a5;
    --green:#6cc25b;
    --sky:#3aa9e0;
    --white:#ffffff;
    --ink:#333333;
    --muted:#8e8e8e;
  }
  *{margin:0;padding:0;box-sizing:border-box}
  html,body{width:1200px;height:1059px;overflow:hidden}
  body{position:relative;font-family:"Arimo",Arial,sans-serif;background:var(--body-mid)}

  .top-band{position:absolute;left:0;top:0;width:1200px;height:148px;background:var(--band-dark)}
  .brand{position:absolute;left:54px;top:95px;display:flex;align-items:center;gap:10px}
  .brand-dot{width:16px;height:16px;border-radius:50%;background:var(--green)}
  .brand-name{font-family:"Nunito",sans-serif;font-weight:700;font-size:31px;color:var(--muted)}
  .brand-tag{position:absolute;left:104px;top:128px;font-family:"Nunito",sans-serif;font-weight:600;font-size:10px;letter-spacing:2px;color:var(--muted)}
  .contact{position:absolute;top:62px;display:flex;align-items:center;gap:10px;font-family:"Nunito",sans-serif;font-weight:600;font-size:24px;white-space:nowrap}
  .contact.web{left:378px;color:var(--green)}
  .contact.mail{left:778px;color:var(--sky)}

  .sheet{position:absolute;left:0;top:148px;width:1200px;height:762px;
    background:radial-gradient(ellipse at 40% 40%,var(--body-light) 0%,var(--body-mid) 55%,var(--body-deep) 100%)}
  .sheet-title{position:absolute;left:0;width:1200px;top:24px;text-align:center;white-space:nowrap;
    font-family:"Michroma",sans-serif;font-size:16px;letter-spacing:5px;color:var(--white);text-transform:uppercase}
  .sheet-title .big{font-size:24px}

  .product-shot{position:absolute;left:69px;top:93px;width:230px;height:635px;
    background:linear-gradient(180deg,#3c3c3c 0%,#4a4a4a 40%,#5d5d5d 100%);border-radius:6px}

  .spec{position:absolute;left:446px;width:615px;border-collapse:separate;border-spacing:0 1px}
  .spec td{font-size:15.5px;line-height:20px;padding:3px 10px;vertical-align:top}
  .spec .key{width:306px;background:var(--teal);color:var(--white)}
  .spec .val{background:var(--white);color:var(--ink);border-left:3px solid transparent}
  .spec.g1{top:93px}.spec.g2{top:266px}.spec.g3{top:436px}.spec.g4{top:608px}

  .footer{position:absolute;left:0;top:910px;width:1200px;height:149px;background:var(--band-dark);color:var(--white)}
  .footer h2{position:absolute;left:0;width:1200px;top:12px;text-align:center;font-weight:400;font-size:17px}
  .perks{position:absolute;top:45px;list-style:none;font-size:15px;line-height:20px;letter-spacing:.5px}
  .perks li{position:relative;padding-left:30px}
  .perks li::before{content:"";position:absolute;left:4px;top:6px;width:8px;height:8px;border-radius:50%;background:var(--white);box-shadow:0 0 6px 2px #d58ac8}
  .perks.left{left:195px}.perks.right{left:620px}
  .venues{position:absolute;left:0;width:1200px;top:118px;text-align:center;font-size:14px;letter-spacing:.3px;white-space:nowrap}
</style>
</head>
<body>
  <header class="top-band">
    <div class="brand"><span class="brand-dot"></span><span class="brand-name">VoltHarbor</span></div>
    <div class="brand-tag">Charging solutions</div>
    <div class="contact web">
      <svg width="28" height="28" viewBox="0 0 28 28" fill="none" stroke="#9a9a9a" stroke-width="1.6"><circle cx="14" cy="14" r="12"/><ellipse cx="14" cy="14" rx="5" ry="12"/><path d="M2 14h24M4 8h20M4 20h20"/></svg>
      <span>www.voltharbor.com</span>
    </div>
    <div class="contact mail">
      <svg width="38" height="26" viewBox="0 0 38 26" fill="none" stroke="#bbbbbb" stroke-width="1.6"><rect x="1" y="1" width="36" height="24"/><path d="M1 1l18 14L37 1M1 25l13-12M37 25L24 13"/></svg>
      <span>info@voltharbor.com</span>
    </div>
  </header>

  <main class="sheet">
    <h1 class="sheet-title"><span class="big">6</span> door phone charging station with pin pad lock</h1>
    <div class="product-shot" role="img" aria-label="Product photo: black six-door phone charging locker with pin pad locks on a floor stand"></div>

    <table class="spec g1">
      <tr><td class="key">Model</td><td class="val">VH - 6</td></tr>
      <tr><td class="key">Lock Type</td><td class="val">Pin Pad Lock</td></tr>
      <tr><td class="key">Over all Dimension</td><td class="val">H580*W420*D170 mm</td></tr>
      <tr><td class="key">Usage</td><td class="val">Nova Phone series, Orbit Phone and other micro USB phone</td></tr>
    </table>
    <table class="spec g2">
      <tr><td class="key">Brand Name</td><td class="val">VoltHarbor</td></tr>
      <tr><td class="key">Material</td><td class="val">Cold Rolled Steel Plate</td></tr>
      <tr><td class="key">Color</td><td class="val">Black / White / Customized</td></tr>
      <tr><td class="key">Structure</td><td class="val">Overall Welding</td></tr>
    </table>
    <table class="spec g3">
      <tr><td class="key">Steel Plate Thickness</td><td class="val">0.5 - 0.8 mm</td></tr>
      <tr><td class="key">Type</td><td class="val">Electric</td></tr>
      <tr><td class="key">Input</td><td class="val">AC 110V - 220 V ( adjustable)</td></tr>
      <tr><td class="key">Output</td><td class="val">DC 5V, 0.5 - 2.1 A</td></tr>
    </table>
    <table class="spec g4">
      <tr><td class="key">Guarantee Period</td><td class="val">6 months</td></tr>
      <tr><td class="key">Certificate</td><td class="val">CE, ROHS</td></tr>
      <tr><td class="key">Packing</td><td class="val">Carton + Wooden Case</td></tr>
      <tr><td class="key">Delivery Time</td><td class="val">25 Days</td></tr>
    </table>
  </main>

  <footer class="footer">
    <h2>Benefits</h2>
    <ul class="perks left">
      <li>Provide customers with a necessary service</li>
      <li>Draw in customers and keep them longer</li>
      <li>Pre-empt “disconnect anxiety”</li>
    </ul>
    <ul class="perks right">
      <li>Strengthens sponsor relationships</li>
      <li>VoltHarbor creates a unique advertising and<br>marketing platform</li>
    </ul>
    <p class="venues">Shopping Malls | Hotel | Lobies | Conference Rooms | Universities | Libraries | Hospitals | Bars | Cafes | Festivals | Events | Train Stations | Limited Options..</p>
  </footer>
</body>
</html>
```